Louisiana personal injury attorney needs a postcard design

This will be the first of three post cards to go out to previous clients. We do not have intentions of making all three match/work with each other, but if you have an idea for that, please, let us know! This is for an attorney in Lafayette, LA that specializes in Medical Malpractice and Personal Injury. We would like the front of the post card to focus on those two practice areas and really grab someones attention!

the card in general will say: Glad to have served you, come see us for a free T-shirt, have a cup of coffee with us…

Please use a photo of the office for us to use on the back with a map of the office location (will send location when we pick the winner)

Industry/Entity Type

Legal

Font styles to use
Serif
Sans Serif

Requirements
Must have
• map of location of office. Large image or several images on the front. attention grabbing
Nice to have
• colors that match the logo. clean and easy to follow
Should not have
• should not be messy or too much going on.

```html
<!DOCTYPE html>
<html lang="en">
<head>
<meta charset="utf-8">
<title>Delcour Law Firm – Postcard</title>
<link href="https://fonts.googleapis.com/css2?family=Marcellus&family=Montserrat:wght@600;700;800&family=Arimo:wght@700&display=swap" rel="stylesheet">
<style>
  :root{
    --gold:#bf9a3e;
    --slate:#666666;
    --ink:#5a5a5a;
    --paper:#ffffff;
    --stripe:#f1f1f1;
    --rule:#d9d9d9;
    --backdrop:#1f1f1f;
    --blue-a:#0a4f9c;
    --blue-b:#2aa7e6;
  }
  *{margin:0;padding:0;box-sizing:border-box}
  html,body{width:973px;height:1200px;overflow:hidden;background:var(--backdrop)}
  .card{position:absolute;left:116px;width:741px;height:494px;background:var(--paper);overflow:hidden}
  .card--front{top:77px}
  .card--back{top:628px}

  /* front */
  .stripes{position:absolute;left:0;top:230px;width:480px;height:264px;
    background:repeating-linear-gradient(to bottom,var(--stripe) 0 6px,transparent 6px 13px)}
  .brand{position:absolute;left:42px;top:30px;width:268px;text-align:center;font-family:"Montserrat",sans-serif;font-weight:800;color:var(--gold)}
  .brand__name{display:block;font-size:54px;line-height:62px;letter-spacing:1px}
  .brand__sub{display:block;font-size:20px;line-height:26px;letter-spacing:14px;margin-top:4px;padding-left:14px}
  .headline{position:absolute;left:42px;top:182px;font-family:"Marcellus",serif;font-size:45px;line-height:53px;color:var(--slate);font-weight:400;white-space:nowrap}
  .hero{position:absolute;left:0;top:0}
  .web-pill{position:absolute;left:42px;top:437px;width:320px;height:48px}
  .web-pill__bar{position:absolute;left:20px;top:7px;right:0;height:32px;border-radius:16px;
    background:linear-gradient(to right,var(--blue-a),var(--blue-b));border:2px solid #cfe9f7}
  .web-pill__text{position:absolute;left:48px;top:13px;font-family:"Montserrat",sans-serif;font-weight:700;font-size:18px;line-height:22px;color:#fff;white-space:nowrap}
  .web-pill__tag{position:absolute;left:0;top:0}

  /* back */
  .office{position:absolute;left:0;top:0}
  .stamp-box{position:absolute;left:630px;top:26px;width:75px;height:69px;border:2px solid #e2e2e2;border-radius:6px}
  .address-line{position:absolute;left:411px;width:293px;height:1px;background:var(--rule)}
  .contact{position:absolute;left:32px;top:362px;font-family:"Arimo",sans-serif;font-weight:700;color:var(--ink)}
  .contact__title{font-size:13px;line-height:18px;margin-bottom:4px}
  .contact__row{display:flex;align-items:center;gap:8px;font-size:12px;height:20px;white-space:nowrap}
  .contact__row svg{width:13px;height:13px;flex:none}
  .location-map{position:absolute;left:227px;top:358px;width:134px;height:102px;border-radius:6px;
    background:linear-gradient(135deg,#e9e3d2 0%,#f3ecd9 40%,#cfe3bf 60%,#e6e1d6 100%)}
</style>
</head>
<body>

<section class="card card--front">
  <div class="stripes"></div>

  <svg class="hero" width="741" height="494" viewBox="0 0 741 494">
    <defs>
      <linearGradient id="buildingTones" x1="0" y1="0" x2="0" y2="1">
        <stop offset="0" stop-color="#c9d3dc"/>
        <stop offset=".3" stop-color="#8e95a0"/>
        <stop offset=".55" stop-color="#4a4b55"/>
        <stop offset=".9" stop-color="#3f4146"/>
        <stop offset="1" stop-color="#5c7a3e"/>
      </linearGradient>
    </defs>
    <circle cx="600" cy="230" r="255" fill="var(--gold)"/>
    <circle cx="565" cy="300" r="240" fill="var(--slate)"/>
    <circle cx="571" cy="254" r="243" fill="#ffffff"/>
    <circle cx="571" cy="254" r="235" fill="url(#buildingTones)" role="img" aria-label="Photo of the law firm building with its name on the facade"/>
  </svg>

  <div class="brand">
    <span class="brand__name">DELCOUR</span>
    <span class="brand__sub">LAW FIRM</span>
  </div>

  <h1 class="headline">GLAD<br>TO HAVE<br>SERVED YOU</h1>

  <div class="web-pill">
    <div class="web-pill__bar"></div>
    <svg class="web-pill__tag" width="44" height="48" viewBox="0 0 44 48">
      <path d="M2 2 L40 24 L2 46 Z" fill="#f2f2f2" stroke="#d0d0d0"/>
      <circle cx="15" cy="24" r="9" fill="#1f6fb5"/>
      <ellipse cx="15" cy="24" rx="4" ry="9" fill="none" stroke="#fff" stroke-width="1"/>
      <line x1="6" y1="24" x2="24" y2="24" stroke="#fff" stroke-width="1"/>
    </svg>
    <span class="web-pill__text">www.delcourlawfirm.com</span>
  </div>
</section>

<section class="card card--back">
  <svg class="office" width="741" height="494" viewBox="0 0 741 494">
    <defs>
      <clipPath id="officeClip">
        <rect x="0" y="0" width="361" height="320"/>
      </clipPath>
      <linearGradient id="officeTones" x1="0" y1="0" x2="1" y2="1">
        <stop offset="0" stop-color="#d8d6d2"/>
        <stop offset=".45" stop-color="#b8b3a6"/>
        <stop offset=".7" stop-color="#4f5a48"/>
        <stop offset="1" stop-color="#6f6a62"/>
      </linearGradient>
    </defs>
    <path d="M361 140 L361 315 C300 313 240 300 180 270 Z" fill="var(--slate)"/>
    <circle cx="-100" cy="-300" r="625" fill="var(--gold)"/>
    <circle cx="-100" cy="-300" r="585" fill="url(#officeTones)" clip-path="url(#officeClip)" role="img" aria-label="Photo of the office conference room"/>
  </svg>

  <div class="stamp-box"></div>
  <div class="address-line" style="top:273px"></div>
  <div class="address-line" style="top:314px"></div>
  <div class="address-line" style="top:355px"></div>
  <div class="address-line" style="top:397px"></div>
  <div class="address-line" style="top:438px"></div>

  <div class="contact">
    <p class="contact__title">Contact:</p>
    <p class="contact__row">
      <svg viewBox="0 0 14 14"><path d="M7 1a4.5 4.5 0 0 0-4.5 4.5C2.5 9 7 13.5 7 13.5S11.5 9 11.5 5.5A4.5 4.5 0 0 0 7 1z" fill="var(--ink)"/><circle cx="7" cy="5.5" r="1.7" fill="#fff"/></svg>
      Address
    </p>
    <p class="contact__row">
      <svg viewBox="0 0 14 14"><circle cx="7" cy="7" r="6.5" fill="var(--ink)"/><path d="M4.5 4 L6 4 L6.6 5.8 L5.7 6.5 C6.2 7.5 6.7 8 7.6 8.4 L8.3 7.5 L10 8.1 L10 9.6 C7 9.8 4.3 7 4.5 4z" fill="#fff"/></svg>
      01.555.010.200
    </p>
    <p class="contact__row">
      <svg viewBox="0 0 14 14"><path d="M13 1 L1 6.5 L5.5 8 L7 13 Z" fill="var(--ink)"/><path d="M13 1 L5.5 8" stroke="#fff" stroke-width="1"/></svg>
      admin@delcourlawfirm.com
    </p>
    <p class="contact__row">
      <svg viewBox="0 0 14 14"><circle cx="7" cy="7" r="6.5" fill="var(--ink)"/><ellipse cx="7" cy="7" rx="3" ry="6.5" fill="none" stroke="#fff" stroke-width=".8"/><line x1=".5" y1="7" x2="13.5" y2="7" stroke="#fff" stroke-width=".8"/></svg>
      www.delcourlawfirm.com
    </p>
  </div>

  <div class="location-map" role="img" aria-label="Map showing the office location"></div>
</section>

</body>
</html>
```